Electrician Business Card/ company logo/small business

New Business Cards and logo needed that will catch peoples eye and say we went that extra step. Attached is a design possibly to be incorporated, if u have your own great, lets see it!... This will be a small local business. thank you for all you do!
Falcon Electric
Dov Merrick Owner
Journeyman Electrician
phone 1.482.639.2075
email: QRTFalconElectric@zentromail.com
call for free estimate!
Updates

Accepted and approved for cards

Target Market(s)

support small local business

Industry/Entity Type

Electrical,

Contact Information for Business Card

name, title,company/ logo, phone, email, free estimate

Font styles to use
Other font styles liked:
• easy to read

Colors

Designer to choose colors to be used in the design.

Requirements
Must have
• eye catching everything! logo and falcon electric listed on business card/logo, incorp logo in the background of card
Nice to have
• lightening bolts in eyes or around the triangle? vertical, modern, any design that would be unique and stand out
Should not have
• pinks, reds, yellows,brown

```html
<!DOCTYPE html>
<html lang="en">
<head>
<meta charset="utf-8">
<title>Falcon Electric – Business Cards</title>
<link href="https://fonts.googleapis.com/css2?family=Poppins:wght@400;500;600&display=swap" rel="stylesheet">
<style>
  :root {
    --page-bg: #1c1c1f;
    --card-deep: #0c0a3a;
    --card-mid: #1a1a7a;
    --card-edge: #2b35b0;
    --glow: #7fb8ff;
    --bolt-core: #dff0ff;
    --brand: #8fd6e8;
    --text-light: #ffffff;
    --text-accent: #f2e21c;
    --icon: #6fd0e0;
  }
  * { margin: 0; padding: 0; box-sizing: border-box; }
  html, body { width: 1200px; height: 1108px; overflow: hidden; }
  body {
    background: var(--page-bg);
    font-family: "Poppins", sans-serif;
    position: relative;
  }
  .card {
    position: absolute;
    top: 154px;
    width: 460px;
    height: 800px;
    border-radius: 20px;
    overflow: hidden;
    background:
      radial-gradient(ellipse 70% 45% at 50% 48%, var(--card-deep) 0%, transparent 100%),
      linear-gradient(180deg, var(--card-edge) 0%, var(--card-mid) 30%, var(--card-deep) 55%, var(--card-mid) 80%, var(--card-edge) 100%);
  }
  .card--front { left: 100px; }
  .card--back { left: 640px; }

  .lightning {
    position: absolute;
    left: 0;
    width: 100%;
    height: 170px;
  }
  .lightning--top {
    top: 0;
    background: radial-gradient(ellipse 80% 60% at 55% 20%, rgba(127,184,255,0.55) 0%, rgba(43,53,176,0.2) 55%, transparent 100%);
  }
  .lightning--bottom {
    bottom: 0;
    background: radial-gradient(ellipse 80% 60% at 45% 85%, rgba(223,240,255,0.5) 0%, rgba(43,53,176,0.2) 55%, transparent 100%);
  }

  .brand {
    position: absolute;
    left: 0;
    width: 100%;
    display: flex;
    align-items: center;
    justify-content: center;
    gap: 14px;
  }
  .brand__dot {
    width: 22px;
    height: 22px;
    border-radius: 50%;
    background: var(--brand);
  }
  .brand__name {
    font-weight: 600;
    font-size: 40px;
    letter-spacing: 6px;
    color: var(--brand);
    text-transform: uppercase;
    line-height: 1.15;
    text-align: center;
  }
  .card--front .brand { top: 330px; }
  .card--back .brand { top: 250px; }

  .contact {
    position: absolute;
    top: 440px;
    left: 0;
    width: 100%;
    text-align: center;
    color: var(--text-light);
  }
  .contact__name {
    font-weight: 500;
    font-size: 24px;
    letter-spacing: 0.5px;
  }
  .contact__role {
    font-weight: 500;
    font-size: 20px;
    color: var(--text-accent);
    margin-top: 2px;
  }
  .contact__icons {
    display: flex;
    align-items: center;
    justify-content: center;
    gap: 10px;
    margin-top: 16px;
  }
  .contact__rule {
    width: 40px;
    height: 1.5px;
    background: var(--icon);
  }
  .contact__icon { width: 30px; height: 30px; }
  .contact__phone {
    font-size: 20px;
    margin-top: 16px;
  }
  .contact__email {
    font-size: 18px;
    margin-top: 6px;
  }
</style>
</head>
<body>

  <section class="card card--front" aria-label="Business card front">
    <div class="lightning lightning--top" role="img" aria-label="Lightning bolts crackling across the top of the card"></div>
    <div class="brand">
      <span class="brand__dot"></span>
      <span class="brand__name">Falcon<br>Electric</span>
    </div>
    <div class="lightning lightning--bottom" role="img" aria-label="Lightning bolts crackling across the bottom of the card"></div>
  </section>

  <section class="card card--back" aria-label="Business card back">
    <div class="lightning lightning--top" role="img" aria-label="Lightning bolts crackling across the top of the card"></div>
    <div class="brand">
      <span class="brand__dot"></span>
      <span class="brand__name">Falcon<br>Electric</span>
    </div>
    <div class="contact">
      <p class="contact__name">DOV MERRICK JOURNEYMAN</p>
      <p class="contact__role">ELECTRICIAN</p>
      <div class="contact__icons">
        <span class="contact__rule"></span>
        <svg class="contact__icon" viewBox="0 0 30 30" aria-hidden="true">
          <circle cx="15" cy="15" r="13" fill="none" stroke="var(--icon)" stroke-width="2"/>
          <path d="M11 9 l3 0 l1 4 l-2 1.5 q1.5 3 4 4 l1.5 -2 l4 1 l0 3 q-8 1 -12 -8 z" fill="var(--icon)"/>
        </svg>
        <svg class="contact__icon" viewBox="0 0 30 30" aria-hidden="true">
          <circle cx="15" cy="15" r="13" fill="none" stroke="var(--icon)" stroke-width="2"/>
          <rect x="8.5" y="10.5" width="13" height="9" rx="1" fill="var(--icon)"/>
          <path d="M8.5 11 l6.5 5 l6.5 -5" fill="none" stroke="var(--card-deep)" stroke-width="1.4"/>
        </svg>
        <span class="contact__rule"></span>
      </div>
      <p class="contact__phone">1.482.639.2075</p>
      <p class="contact__email">QRTFalconElectric@zentromail.com</p>
    </div>
    <div class="lightning lightning--bottom" role="img" aria-label="Lightning bolts crackling across the bottom of the card"></div>
  </section>

</body>
</html>
```